Web Design - Personal Item Tags Portal

web page designs need to be created for a new company that provides item tracking tags and lets users register and report stolen/found items.
The theme of the designs needs to be energetic and convey a sense of freedom and adventure - where the user does not have to worry about their items since they have all been "tagged".
the client likes parts of the site at: http://www.plimcraft.example/
they like:
1. slider images at top of pages. large slider on front page. fixed smaller height picture on internal pages
2. fixed company message on left-hand-side
3. My Account button to be clear and stand out

other comments:
clean, simple
• brand focused
• will have clear call to actions
• will include a description of what and why
• will appeal to both males and females

sections that the website will have are:
Home
About Us
How it works
Why
Case Studies
Uses and Applications
Shop
Contact Us

please create 2 designs : 1 home page, 1 internal page

Final winner will also require HTML slicing to be done.

hi, i have now updated the images so they work. sorry!

Hi, looking at all the designs that are coming in, alot of them are great. Designers need to remember to make the register for an account button more prominent. Also, there should be a "report found" and "report lost" buttons on the front-page and should be prominent as well.

Thanks

Hi, the customer has come back with a few comments and modifications for the designs, if you are able to make some tweaks to your submissions, that will be great:

The client would like the designs to be modified to highlight 3 main actions:
1. Log In/Register
2. Find an Owner
3. Lost an Item

The home page shouldnt be too content heavy in terms of text, it should only have major highlight points of what the system does (the 3 points listed above). the inner page designs are OK to have more text though.

i will also upload some notes from the customer that can be used as a guide and also include the design styles which the customer likes (but is not entirely happy with).

uploaded image files (3) with customer feedback comments

```html
<!DOCTYPE html>
<html lang="en">
<head>
<meta charset="utf-8">
<title>Roamtag – Home</title>
<link href="https://fonts.googleapis.com/css2?family=Bree+Serif&family=Titillium+Web:wght@400;600&family=Open+Sans:wght@400;600&display=swap" rel="stylesheet">
<style>
:root{
  --ink:#141414;
  --green:#35b85e;
  --green-dark:#27a04d;
  --teal-dark:#2c4a48;
  --teal:#4f7d78;
  --text:#555;
  --heading:#333;
  --card-border:#dcdcdc;
  --footer:#d6d6d6;
  --footer-text:#888;
}
*{box-sizing:border-box;margin:0;padding:0}
html,body{width:1200px;height:1143px;overflow:hidden}
body{position:relative;background:#fff;font-family:"Open Sans",sans-serif;color:var(--text)}
.abs{position:absolute}
.site-header{left:0;top:0;width:1200px;height:90px;background:var(--ink)}
.brand{left:150px;top:18px;display:flex;align-items:center;gap:12px}
.brand-mark{width:44px;height:44px;border:3px solid #fff;border-radius:50%}
.brand-name{font-family:"Titillium Web",sans-serif;font-weight:600;font-size:40px;color:#fff;line-height:1}
.social{left:862px;top:36px;display:flex;gap:9px}
.social span{width:16px;height:16px;background:var(--green);border-radius:2px;display:block}
.account-btn{left:960px;top:30px;width:132px;height:27px;border-radius:14px;background:var(--green);color:#fff;font-family:"Bree Serif",serif;font-size:12px;display:flex;align-items:center;justify-content:center;gap:8px}
.account-btn svg{width:10px;height:12px}
.main-nav{left:0;top:90px;width:1200px;height:47px;background:linear-gradient(#3d5654,#2a3f3e);border-bottom:1px solid #52706c}
.main-nav a{position:absolute;top:0;height:47px;line-height:47px;color:#fff;font-family:"Bree Serif",serif;font-size:13.5px;text-decoration:none;transform:translateX(-50%);white-space:nowrap}
.main-nav .current{left:142px;width:94px;transform:none;text-align:center;background:linear-gradient(#26312f,#1d2625)}
.hero{left:0;top:137px;width:1200px;height:353px;background:radial-gradient(ellipse 70% 90% at 75% 100%,#b7e0cc 0%,#6f9f94 40%,#3f6763 75%,#2f4e4b 100%)}
.hero h1{position:absolute;left:0;width:1200px;top:32px;text-align:center;font-family:"Titillium Web",sans-serif;font-weight:600;font-size:40px;color:#fff;line-height:1}
.hero p{position:absolute;left:0;width:1200px;top:74px;text-align:center;font-family:"Titillium Web",sans-serif;font-size:22px;color:#fff;line-height:1}
.register-btn{position:absolute;left:446px;top:131px;width:308px;height:43px;border-radius:22px;background:var(--green);color:#fff;font-family:"Bree Serif",serif;font-size:19px;display:flex;align-items:center;justify-content:center;box-shadow:0 2px 3px rgba(0,0,0,.25)}
.hero-devices{position:absolute;left:400px;top:215px;width:520px;height:138px;background:linear-gradient(90deg,#2a2a2a 0%,#111 30%,#2a6fb3 55%,#a9b4bb 100%);border-radius:10px 10px 0 0}
.card{background:#fafafa;border:1px solid var(--card-border);box-shadow:0 1px 2px rgba(0,0,0,.12)}
.card h2{font-family:"Titillium Web",sans-serif;font-weight:400;font-size:23px;color:var(--heading);line-height:1}
.action-card{text-align:center;padding-top:16px}
.action-card p{font-size:11px;line-height:14px;margin:12px 18px 0}
.green-btn{display:inline-flex;align-items:center;justify-content:center;width:132px;height:28px;border-radius:14px;background:var(--green);color:#fff;font-family:"Bree Serif",serif;font-size:12.5px;margin-top:10px}
.grey-btn{display:inline-flex;align-items:center;justify-content:center;width:95px;height:29px;border-radius:15px;background:linear-gradient(#fff,#e7e7e7);border:1px solid #ccc;color:#444;font-family:"Bree Serif",serif;font-size:12.5px}
.why{left:141px;top:672px;width:640px}
.why h2{font-family:"Titillium Web",sans-serif;font-weight:600;font-size:34px;color:var(--heading);line-height:1}
.why p{font-size:11px;line-height:14px;margin-top:14px}
.why p:first-of-type{margin-top:26px}
.why .grey-btn{margin-top:26px}
.quote-card{padding:14px 0 0 14px}
.portrait{position:absolute;left:16px;top:70px;width:71px;height:62px;background:linear-gradient(#7a7a7a,#2e2e2e)}
.quote-mark{position:absolute;font-family:"Titillium Web",sans-serif;font-weight:600;font-size:40px;color:#aaa;line-height:1}
.quote-text{position:absolute;left:116px;top:62px;width:190px;font-size:11px;line-height:14px}
.quote-name{position:absolute;left:116px;top:122px;font-family:"Titillium Web",sans-serif;font-weight:600;font-size:13px;color:#222}
.dots{position:absolute;left:261px;top:151px;display:flex;gap:6px}
.dots span{width:14px;height:14px;border-radius:50%;border:1px solid #aaa;background:#fff}
.dots .on{background:var(--green);border-color:var(--green)}
.uses-card{padding:16px 0 0 36px}
.uses-list{list-style:none;margin-top:14px}
.uses-list li{position:relative;padding-left:7px;margin-bottom:14px;font-size:11px;line-height:14px;width:270px}
.uses-list li::before{content:"➾";position:absolute;left:-12px;top:0;font-size:8px;color:#777}
.uses-list strong{display:block;font-weight:600;color:#222}
.latest{padding:8px 0 0 6px}
.latest h2{font-size:17px}
.latest-inner{position:absolute;left:5px;top:33px;width:238px;height:486px;background:#fff;border:1px solid #e2e2e2;text-align:center}
.item-pic{margin:24px auto 0}
.item-title{font-family:"Titillium Web",sans-serif;font-weight:600;font-size:13px;color:#222;margin-top:16px}
.item-text{font-size:11px;line-height:14px;margin:6px 24px 0}
.latest-inner .grey-btn{margin-top:13px}
.view-all{position:absolute;left:15px;top:522px;font-family:"Titillium Web",sans-serif;font-weight:600;font-size:12px;color:#222}
.site-footer{left:0;top:1080px;width:1200px;height:63px;background:var(--footer);border-top:1px solid #c8c8c8;text-align:center;font-family:"Bree Serif",serif;font-size:10px;color:var(--footer-text);padding-top:16px;line-height:13px}
</style>
</head>
<body>
<header class="site-header abs">
  <div class="brand abs"><span class="brand-mark"></span><span class="brand-name">Roamtag</span></div>
  <div class="social abs">
    <span aria-label="Video channel"></span><span aria-label="Social page"></span><span aria-label="Updates feed"></span>
  </div>
  <div class="account-btn abs"><svg viewBox="0 0 10 12"><rect x="1" y="5" width="8" height="7" fill="#fff"/><path d="M3 5V3a2 2 0 0 1 4 0v2" stroke="#fff" stroke-width="1.4" fill="none"/></svg>My Account</div>
</header>
<nav class="main-nav abs">
  <a class="current">Home</a>
  <a style="left:285px">About Us</a>
  <a style="left:400px">How it works</a>
  <a style="left:501px">Why</a>
  <a style="left:602px">Case Studies</a>
  <a style="left:760px">Uses and Applications</a>
  <a style="left:893px">Shop</a>
  <a style="left:998px">Contact Us</a>
</nav>
<section class="hero abs">
  <h1>Stolen Items can be found easily</h1>
  <p>You can report any lost items here</p>
  <div class="register-btn">Register for an account</div>
  <div class="hero-devices" role="img" aria-label="Camera, smartphone and laptop grouped together"></div>
</section>

<div class="card action-card abs" style="left:141px;top:509px;width:317px;height:136px">
  <h2>Have you found any items</h2>
  <p>Ut wisi enim ad minim veniam, quis nostrud exerci tation-suscipit lobortis nisl ut aliquip ex ea commodo</p>
  <span class="green-btn">Report found</span>
</div>
<div class="card action-card abs" style="left:476px;top:509px;width:316px;height:136px">
  <h2>Have you lost any items</h2>
  <p>Ut wisi enim ad minim veniam, quis nostrud exerci tation ullamcorper suscipit lobortis nisl ut aliquip</p>
  <span class="green-btn">Report lost</span>
</div>

<section class="why abs">
  <h2>Why we are better</h2>
  <p>Ut wisi enim ad minim veniam, quis nostrud exerci tation ullamcorper suscipit lobortis nisl ut aliquip ex ea commodo consequat. Duis autem vel eum iriure dolor in hendrerit in vulputate velit esse molestie consequat,</p>
  <p>vel illum dolore eu feugiat nulla facilisis at vero eros et accumsan et iusto odio dignissim qui blandit praesent luptatum zzril delenit augue duis dolore te feugait nulla facilisi.</p>
  <span class="grey-btn">More</span>
</section>

<div class="card quote-card abs" style="left:141px;top:881px;width:317px;height:171px">
  <h2>What People say!</h2>
  <div class="portrait" role="img" aria-label="Portrait photo of the customer"></div>
  <span class="quote-mark" style="left:90px;top:44px">“</span>
  <p class="quote-text">Ut wisi enim ad minim veniam, quis nostrud exerci tation ullamcorper suscipit lobortis nisl ut aliquip ex ea commodo consequat.</p>
  <span class="quote-name">Martin Hale - Westbury</span>
  <span class="quote-mark" style="left:288px;top:112px">”</span>
  <div class="dots"><span class="on"></span><span></span><span></span></div>
</div>

<div class="card uses-card abs" style="left:476px;top:881px;width:316px;height:171px">
  <h2>Uses &amp; Applications</h2>
  <ul class="uses-list">
    <li><strong>praesent luptatum</strong>Typi non habent claritatem insitam; est usus legentis in iis qui facit</li>
    <li><strong>praesent luptatum</strong>Typi non habent claritatem insitam; est usus legentis in iis qui facit</li>
  </ul>
</div>

<aside class="card latest abs" style="left:808px;top:508px;width:249px;height:544px">
  <h2>Latest Items</h2>
  <div class="latest-inner">
    <div class="item-pic" role="img" aria-label="Laptop product photo" style="width:128px;height:102px;background:linear-gradient(#1f5e9c,#9aa3a9)"></div>
    <p class="item-title">imperdiet doming</p>
    <p class="item-text">Typi non habent claritatem insitam; est usus legentis in iis qui facit</p>
    <span class="grey-btn">Shop now</span>
    <div class="item-pic" role="img" aria-label="Smartphone product photo" style="width:48px;height:96px;margin-top:26px;border-radius:6px;background:linear-gradient(#222,#3a5e8c,#222)"></div>
    <p class="item-title">imperdiet doming</p>
    <p class="item-text">Typi non habent claritatem insitam; est usus legentis in iis qui facit</p>
    <span class="grey-btn">Shop Now</span>
  </div>
  <span class="view-all">View all</span>
</aside>

<footer class="site-footer abs">
  <div>Home &nbsp;|&nbsp; About Us &nbsp;|&nbsp; How it works &nbsp;|&nbsp; Why &nbsp;|&nbsp; Case Studies &nbsp;|&nbsp; Uses and Applications &nbsp;|&nbsp; Shop &nbsp;|&nbsp; Contact Us</div>
  <div>@Copyrights 2013 roamtag.example &nbsp;|&nbsp; All rights reserved</div>
</footer>
</body>
</html>
```